Dog themed post card for homeowners that may be willing to sell their house.

We will be sending these postcards to homeowners that may be interested in selling their house. Our business is themed around our dog "Wexley"- Wexley Buys Houses. We are using her as the focal point of the business because typically these homeowners get lots of mailers that are similar and we would like stand out with an inviting puppy dog.
We would like to included the icon for facebook and instragam with her handle "@WexleyBuysHouses" and her website WexleyBuysHouses.example and our phone number 555-814-2760.
We will be sending these postcards in batches to various subdivisions. For that reason please consider a format that can easily change the name of the subdivision. We are including the subdivision name because we want the postcard to be slightly more personal/targeted.
Our business is just starting and we would like to get some brand recognition going. We envision Wexley Buys Houses predominately displayed somehow.
I have attached numerous pictures of Wexley. We envision using one on each side of the postcard. Below are phrases we would like to include on the postcard in a format that you see fitting. Please use the verbiage below and not what is sketched on the uploaded postcard. The below verbiage is the most up to date.
-I recently bought a house in (subdivision name) and would love to buy yours.
-Call my humans today so we can give you a no obligation offer
-No money out of your pocket
-Quick closing
-Any condition
-Can help with moving expenses

Target Market(s)

Home owners with equity in their house that may need to sell quickly. These are generally people that do not enjoy the buying/selling of real estate. It can sometimes be someone who has recently inherited a home and doesnt want to deal with the headache. Other times it may be someone going through a divorce or forclosure and want to sell their home quickly.

Industry/Entity Type

Direct Marketing

Requirements
Must have
• Happy and bright feel. This industry is saturated with less than ethical people and we are trying to convey a very clean, honest, straight forward and scam-free process.

```html
<!DOCTYPE html>
<html lang="en">
<head>
<meta charset="utf-8">
<title>Wexley Buys Houses – Postcard</title>
<link href="https://fonts.googleapis.com/css2?family=Open+Sans:ital,wght@0,300;0,400;0,600;0,700;1,600&display=swap" rel="stylesheet">
<style>
  :root{
    --yellow:#dcc232;
    --charcoal:#4a4a4a;
    --ink:#3f3f3f;
    --mist:#f0eeee;
    --paper:#ffffff;
    --hero-top:#cfcfcb;
    --hero-bottom:#b3a38c;
    --thumb-dog-top:#cfccc6;
    --thumb-dog-bottom:#ad9e8a;
    --thumb-house-top:#bf8f7a;
    --thumb-house-bottom:#a96f58;
    --portrait-top:#d6d6d4;
    --portrait-bottom:#a8a6a2;
  }
  *{margin:0;padding:0;box-sizing:border-box}
  html,body{width:1200px;height:1200px;overflow:hidden;background:var(--paper)}
  body{font-family:"Open Sans",Arial,sans-serif;color:var(--ink);position:relative}
  .card{position:absolute;left:194px;width:820px;height:547px;background:var(--paper);overflow:hidden;box-shadow:0 3px 10px rgba(0,0,0,.25)}
  .card--front{top:44px}
  .card--back{top:617px}
  .abs{position:absolute}
  .nowrap{white-space:nowrap}

  /* front */
  .front__header{left:0;top:0;width:820px;height:141px;background:var(--mist)}
  .brand{left:16px;top:6px;line-height:1}
  .brand__name{display:block;font-weight:700;font-size:62px;color:var(--yellow);letter-spacing:-1px}
  .brand__tag{display:block;font-weight:400;font-size:56px;color:var(--ink);margin-top:2px;letter-spacing:-1px}
  .intro{left:18px;top:159px;width:362px;font-size:17.5px;font-weight:600;line-height:21px;color:var(--charcoal)}
  .intro p+p{margin-top:18px}
  .blank{display:inline-block;width:100px;border-bottom:1.5px solid var(--ink);margin-left:8px;vertical-align:4px}
  .perks{left:18px;top:282px;list-style:none;font-size:18px;font-weight:300;line-height:21px;color:var(--ink)}
  .perks li{display:flex;align-items:center;gap:6px;white-space:nowrap}
  .tick{width:20px;height:18px;flex:none}
  .hero-photo{left:386px;top:16px;width:414px;height:375px;border:3px solid var(--yellow);background:linear-gradient(180deg,var(--hero-top),var(--hero-bottom))}
  .contact-band{left:0;top:392px;width:376px;height:155px;background:var(--charcoal)}
  .follow-band{left:376px;top:392px;width:444px;height:155px;background:var(--yellow)}
  .thumb{top:392px;height:107px;border:3px solid var(--paper)}
  .thumb--dog{left:386px;width:204px;background:linear-gradient(180deg,var(--thumb-dog-top),var(--thumb-dog-bottom))}
  .thumb--house{left:596px;width:205px;background:linear-gradient(180deg,var(--thumb-house-top),var(--thumb-house-bottom))}
  .follow{left:472px;top:508px;display:flex;align-items:center;gap:8px}
  .follow__label{font-style:italic;font-weight:600;font-size:19px;color:var(--charcoal);margin-right:4px}
  .follow__dot{width:16px;height:16px;border-radius:50%;background:var(--charcoal)}
  .follow__handle{font-size:11px;font-weight:600;color:var(--charcoal)}

  .call{color:var(--paper)}
  .call__icon{width:44px;height:54px}
  .call__lead{font-style:italic;font-weight:600;font-size:23px;line-height:1;color:var(--paper);white-space:nowrap}
  .call__number{font-weight:700;font-size:37px;line-height:1;color:var(--yellow);letter-spacing:-.3px;white-space:nowrap}
  .info-row{display:flex;align-items:center;gap:14px;font-size:18px;font-weight:400;white-space:nowrap}
  .info-row svg{width:24px;height:18px;flex:none}
  .info-row--back{font-size:16px;gap:12px}

  /* back */
  .back__intro{left:0;top:0;width:456px;height:158px;background:var(--mist)}
  .back__how{left:0;top:158px;width:456px;height:300px;background:var(--yellow)}
  .back__cta{left:0;top:458px;width:456px;height:89px;background:var(--charcoal)}
  .headline{left:22px;top:16px;font-weight:700;font-size:30px;line-height:29px;text-transform:uppercase}
  .headline span{display:block;color:var(--yellow)}
  .headline strong{display:block;color:var(--ink)}
  .pitch{left:22px;top:86px;width:430px;font-size:11.6px;line-height:14px;color:var(--ink);white-space:nowrap}
  .how__title{left:20px;top:170px;font-weight:700;font-size:22px;color:var(--paper);border-bottom:2px solid var(--paper);line-height:28px}
  .steps{left:20px;top:210px;width:430px;list-style:none;color:var(--paper);font-size:19.5px;line-height:26px;font-weight:400}
  .steps li{display:flex;gap:6px;white-space:nowrap}
  .steps .tick{margin-top:4px}
  .cta{left:0;top:466px;width:456px;text-align:center;font-size:14px;font-weight:700;line-height:18px;color:var(--paper)}
  .cta__title{color:var(--yellow)}
  .return{left:477px;top:18px;font-size:12.5px;line-height:15px;color:var(--ink);font-style:normal}
  .return b{font-weight:700;color:var(--charcoal)}
  .stamp{left:719px;top:20px;width:76px;height:76px;border:1px solid var(--ink)}
  .addr-line{left:477px;width:318px;border-top:1px dashed #777}
  .portrait{left:574px;top:285px;width:115px;height:115px;border-radius:50%;border:4px solid var(--yellow);background:linear-gradient(180deg,var(--portrait-top),var(--portrait-bottom))}
</style>
</head>
<body>

<svg width="0" height="0" style="position:absolute">
  <defs>
    <symbol id="tick" viewBox="0 0 20 18"><path d="M2 9 L8 15 L18 2" fill="none" stroke="currentColor" stroke-width="3.5" stroke-linecap="round" stroke-linejoin="round"/></symbol>
    <symbol id="phone" viewBox="0 0 44 54"><rect x="2" y="4" width="11" height="48" rx="3" fill="none" stroke="currentColor" stroke-width="3"/><rect x="13" y="10" width="29" height="42" rx="3" fill="none" stroke="currentColor" stroke-width="3"/><rect x="19" y="16" width="17" height="7" fill="currentColor"/><g fill="currentColor"><rect x="19" y="28" width="4" height="4"/><rect x="26" y="28" width="4" height="4"/><rect x="33" y="28" width="4" height="4"/><rect x="19" y="35" width="4" height="4"/><rect x="26" y="35" width="4" height="4"/><rect x="33" y="35" width="4" height="4"/><rect x="19" y="42" width="4" height="4"/><rect x="26" y="42" width="4" height="4"/><rect x="33" y="42" width="4" height="4"/></g></symbol>
    <symbol id="mail" viewBox="0 0 24 18"><rect x="1" y="2" width="22" height="14" fill="none" stroke="currentColor" stroke-width="2"/><path d="M1 2 L12 11 L23 2" fill="none" stroke="currentColor" stroke-width="2"/></symbol>
    <symbol id="globe" viewBox="0 0 24 18"><circle cx="12" cy="9" r="8" fill="none" stroke="currentColor" stroke-width="2"/><path d="M4 9 H20 M12 1 C8 5 8 13 12 17 M12 1 C16 5 16 13 12 17" fill="none" stroke="currentColor" stroke-width="1.5"/></symbol>
  </defs>
</svg>

<section class="card card--front">
  <div class="abs front__header"></div>
  <h1 class="abs brand"><span class="brand__name">WEXLEY</span><span class="brand__tag">BUYS HOUSES</span></h1>

  <div class="abs intro">
    <p><span class="nowrap">I recently bought a house in<span class="blank"></span></span><br>and would love to buy yours.</p>
    <p><span class="nowrap">Call my humans today so we can give you</span><br>a no obligation offer</p>
  </div>

  <ul class="abs perks">
    <li><svg class="tick" style="color:var(--yellow)"><use href="#tick"/></svg>No money out of your pocket</li>
    <li><svg class="tick" style="color:var(--yellow)"><use href="#tick"/></svg>Quick closing</li>
    <li><svg class="tick" style="color:var(--yellow)"><use href="#tick"/></svg>Any condition</li>
    <li><svg class="tick" style="color:var(--yellow)"><use href="#tick"/></svg>Can help with moving expenses</li>
  </ul>

  <div class="abs hero-photo" role="img" aria-label="Photo of Wexley, a fluffy grey dog in a striped bandana, sitting on a front lawn"></div>

  <div class="abs contact-band"></div>
  <div class="abs follow-band"></div>
  <div class="abs thumb thumb--dog" role="img" aria-label="Photo of Wexley sitting on a garden path"></div>
  <div class="abs thumb thumb--house" role="img" aria-label="Photo of a brick house with a garage"></div>

  <div class="abs follow">
    <span class="follow__label">Follow us</span>
    <span class="follow__dot"></span>
    <span class="follow__dot"></span>
    <span class="follow__handle">@WexleyBuysHouses</span>
  </div>

  <svg class="abs call__icon" style="left:15px;top:410px;color:var(--paper)"><use href="#phone"/></svg>
  <div class="abs call" style="left:70px;top:404px">
    <div class="call__lead">Call my humans today!</div>
    <div class="call__number" style="margin-top:4px">(555) 814-2760</div>
  </div>
  <div class="abs info-row" style="left:32px;top:481px;color:var(--paper)"><svg><use href="#mail"/></svg>WexleyBuysHouses@example.com</div>
  <div class="abs info-row" style="left:32px;top:511px;color:var(--paper)"><svg><use href="#globe"/></svg>www.WexleyBuysHouses.example</div>
</section>

<section class="card card--back">
  <div class="abs back__intro"></div>
  <div class="abs back__how"></div>
  <div class="abs back__cta"></div>

  <h2 class="abs headline"><span>Need to sell your</span><strong>home right away?</strong></h2>
  <p class="abs pitch">Wexley specialize in quickly acquiring problem properties and solving your<br>selling headaches, with no B.S. and no commissions.<br>Wexley invite you to call us right now for a NO obligation consultation and<br>a fast and fair offer to sell your house so you can move forward with your life.</p>

  <h3 class="abs how__title">HOW IT WORKS !</h3>
  <ul class="abs steps">
    <li><svg class="tick" style="color:var(--charcoal)"><use href="#tick"/></svg><span>Tell us about your property</span></li>
    <li><svg class="tick" style="color:var(--charcoal)"><use href="#tick"/></svg><span>If it meets our buying criteria, Wexley’ll<br>contact you to set up a quick appointment<br>and walk through.</span></li>
    <li><svg class="tick" style="color:var(--charcoal)"><use href="#tick"/></svg><span>Wexley’ll present you with a fair written,<br>no-obligation offer</span></li>
    <li><svg class="tick" style="color:var(--charcoal)"><use href="#tick"/></svg><span>Wexley close with our reputable<br>Real Estate Attorney, at a closing date<br>of your choice.</span></li>
  </ul>

  <div class="abs cta">
    <div class="cta__title">GET STARTED NOW!</div>
    <div>Wexley buy houses in any condition.</div>
    <div>giving us some information about your property By</div>
    <div>call or text (555) 814-2760</div>
  </div>

  <address class="abs return"><b>Wexley Buys Houses</b><br>PO Box 0000 Brackton,<br>DD&nbsp; 00000</address>
  <div class="abs stamp"></div>
  <div class="abs addr-line" style="top:158px"></div>
  <div class="abs addr-line" style="top:193px"></div>
  <div class="abs addr-line" style="top:228px"></div>
  <div class="abs addr-line" style="top:263px"></div>

  <div class="abs portrait" role="img" aria-label="Round photo of Wexley the dog wearing a bandana"></div>

  <svg class="abs call__icon" style="left:478px;top:414px;color:var(--charcoal)"><use href="#phone"/></svg>
  <div class="abs" style="left:531px;top:410px">
    <div class="call__lead" style="color:var(--charcoal)">Call my humans today!</div>
    <div class="call__number" style="margin-top:4px">(555) 814-2760</div>
  </div>
  <div class="abs info-row info-row--back" style="left:494px;top:484px;color:var(--charcoal)"><svg><use href="#mail"/></svg>WexleyBuysHouses@example.com</div>
  <div class="abs info-row info-row--back" style="left:494px;top:510px;color:var(--charcoal)"><svg><use href="#globe"/></svg>www.WexleyBuysHouses.example</div>
</section>

</body>
</html>
```